Business card design needed

I need a business card for my new Food & Lifestyle Coaching business - "Bloomvale Food & Lifestlye Coaching"

i already have a logo and would like to have that incorporated into the business card, obviously.

i would like a design that says "fresh" and "funky" - my target market is female, aged 20-45 so i want something that will stand out to them when they see it.

My "Company Colour" is Apple Green
Updates

Thankyou to everyone who has submitted a design for my project. At this stage i have quite a large number of designs to chose from and with only a short time until my project closes i am focusing now on chosing from those i have already shortlisted so am unfortunately not considering any new desings.

Thankyou again for your interest in my project.

Target Market(s)

Female, Health Conscious (or looking to improve their health/lifestyle), aged between 20-45

Industry/Entity Type

Business

Contact Information for Business Card

Tamsin Corley
Ph: 0417382946
Email: eatwell@marovex.com

Requirements
Must have
• Must include my existing Logo
Nice to have
• Would be nice to incoirporate and appointment card on the back

```html
<!DOCTYPE html>
<html lang="en">
<head>
<meta charset="utf-8">
<title>Bloomvale Food &amp; Lifestlye Coaching – Business Card</title>
<link rel="stylesheet" href="https://fonts.googleapis.com/css2?family=Josefin+Slab:wght@300;400&family=Open+Sans:wght@400&display=swap">
<style>
  :root {
    --apple-green: #95c12b;
    --apple-green-light: #a9cf3f;
    --card-white: #ffffff;
    --ink: #3a3a3a;
    --ink-soft: #4d4d4d;
    --rule: #5f7a1c;
    --backdrop: #dfe5e8;
  }
  * { box-sizing: border-box; margin: 0; padding: 0; }
  html, body {
    width: 1200px; height: 960px; overflow: hidden;
    background: var(--backdrop);
  }
  .canvas {
    position: relative; width: 1200px; height: 960px;
  }
  .card {
    position: absolute; left: 320px; width: 560px; height: 320px;
    box-shadow: 0 6px 18px rgba(0,0,0,.18);
    overflow: hidden;
  }
  .card--front { top: 110px; background: var(--card-white); }
  .card--back {
    top: 530px;
    background: linear-gradient(120deg, var(--apple-green) 0%, var(--apple-green) 60%, var(--apple-green-light) 100%);
  }

  .brand-name {
    font-family: "Josefin Slab", serif; font-weight: 400;
    color: var(--ink); line-height: 1;
  }
  .brand-name__main { display: block; font-size: 52px; letter-spacing: 1px; }
  .brand-name__tag { display: block; font-size: 14px; margin-top: 6px; }

  .card--front .brand-name { position: absolute; left: 300px; top: 38px; }
  .accent-dot {
    position: absolute; left: 40px; top: 40px;
    width: 150px; height: 150px; border-radius: 50%;
    background: var(--apple-green);
  }

  .holder {
    position: absolute; left: 300px; top: 184px;
    display: flex; align-items: center; gap: 14px;
  }
  .holder__mark { width: 14px; height: 14px; border-radius: 50%; background: var(--apple-green); }
  .holder__name {
    font-family: "Josefin Slab", serif; font-weight: 400;
    font-size: 26px; color: var(--ink);
  }

  .contact-list {
    position: absolute; left: 300px; top: 244px; list-style: none;
    font-family: "Open Sans", sans-serif; font-size: 15px; color: var(--ink-soft);
  }
  .contact-list li { display: flex; align-items: center; gap: 10px; height: 24px; }
  .contact-list svg { width: 15px; height: 15px; }

  .card--back .brand-name { position: absolute; left: 150px; top: 36px; color: var(--card-white); }
  .card--back .brand-name__tag { color: var(--ink); }

  .appointment__title {
    position: absolute; left: 0; right: 0; top: 150px; text-align: center;
    font-family: "Josefin Slab", serif; font-weight: 400;
    font-size: 18px; letter-spacing: 2px; color: var(--ink);
  }
  .appointment__line {
    position: absolute; left: 40px; right: 40px; height: 1px; background: var(--rule);
  }
</style>
</head>
<body>
<main class="canvas">

  <section class="card card--front" aria-label="Business card front">
    <div class="accent-dot" aria-hidden="true"></div>
    <div class="brand-name">
      <span class="brand-name__main">Bloomvale</span>
      <span class="brand-name__tag">Food &amp; Lifestlye Coaching</span>
    </div>
    <div class="holder">
      <span class="holder__mark" aria-hidden="true"></span>
      <span class="holder__name">Tamsin Corley</span>
    </div>
    <ul class="contact-list">
      <li>
        <svg viewBox="0 0 16 16" aria-hidden="true"><rect x="4" y="1" width="8" height="14" rx="1.5" fill="none" stroke="#3a3a3a" stroke-width="1.4"/><rect x="5.5" y="3" width="5" height="5" fill="#3a3a3a"/></svg>
        <span>0417382946</span>
      </li>
      <li>
        <svg viewBox="0 0 16 16" aria-hidden="true"><rect x="1" y="3" width="14" height="10" fill="none" stroke="#3a3a3a" stroke-width="1.4"/><path d="M1 3 L8 9 L15 3 M1 13 L6 8 M15 13 L10 8" fill="none" stroke="#3a3a3a" stroke-width="1.2"/></svg>
        <span>eatwell@marovex.com</span>
      </li>
    </ul>
  </section>

  <section class="card card--back" aria-label="Appointment card back">
    <div class="brand-name">
      <span class="brand-name__main">Bloomvale</span>
      <span class="brand-name__tag">Food &amp; Lifestlye Coaching</span>
    </div>
    <h2 class="appointment__title">NEXT APPOINTMENT</h2>
    <div class="appointment__line" style="top:200px"></div>
    <div class="appointment__line" style="top:236px"></div>
    <div class="appointment__line" style="top:272px"></div>
  </section>

</main>
</body>
</html>
```